uk based ecommerce website requires fresh look ,high quality look and feel

we are a web based company selling eco friendly ground reinforcement grids to diy and construction sectors
our existing website is www.plumbrookpaving.co.uk ,

we have already updated the logo so that is the branding sorted .so we need a ecommerce website that is very much up-to date in design and layout and which has content management system for ease of use so that we can add products and information as required.

Use current logo as reference for colour scheme.
www.plumbrookpaving.co.uk

The current website has 6 pages accessible through the navigation bar, I would now like 5 pages, removing the need for the Trade Enquiries page possibly have it with along with contact us.

Target Market(s)

construction industry , diy end users,
retail market, landscapers, gardeners

Industry/Entity Type

Construction

Font styles to use
Other font styles liked:
• logo font prometo

Colors
f78f20
9bcb3c

Requirements
Must have
• logo colours and logo design in website with cms responsive design for tablet and mobile devices
• expect content to work flawlessly and look great across all devices
• HTML 5 custom design with coding as required
• must have good experiance in ecommerce website design
• eye catching, high quality look and feel and very user friedly ,very up-to date.
Nice to have
• picture slider show
• explain in writing what exactly i am getting in my ecommerce website
Should not have
• plain , basic design , old fashion looking ,cheap look

```html
<!DOCTYPE html>
<html lang="en">
<head>
<meta charset="utf-8">
<title>Plumbrook Ground Solutions – Contact Us</title>
<link rel="stylesheet" href="https://fonts.googleapis.com/css2?family=Open+Sans:wght@400;600;700&family=Audiowide&display=swap">
<style>
:root{
  --orange:#f78f20;
  --green:#9bcb3c;
  --green-dark:#7fb02a;
  --page-bg:#74a82c;
  --ink:#555;
  --line:#d9d9d9;
  --footer:#2e2e2e;
  --footer-text:#cfcfcf;
  --refresh:#1e88d6;
}
*{box-sizing:border-box;margin:0;padding:0}
html,body{width:812px;height:1200px;overflow:hidden}
body{background:var(--page-bg);font-family:"Open Sans",Arial,sans-serif;color:var(--ink);position:relative}
.page{position:absolute;left:45px;top:0;width:722px;height:1200px;background:#fff}
.abs{position:absolute}

.utility-bar{left:0;top:0;width:722px;height:16px;background:var(--orange);display:flex;justify-content:flex-end;align-items:center;padding-right:23px;gap:14px;font-size:6.5px;color:#fff;text-transform:uppercase}
.utility-bar .sep{opacity:.8}

.brand{left:23px;top:37px;display:flex;align-items:center;gap:7px}
.brand-mark{width:22px;height:22px;border-radius:50%;background:var(--green)}
.brand-name{font-weight:700;font-size:11px;color:var(--orange);text-transform:uppercase;white-space:nowrap}
.search{left:434px;top:42px;width:157px;height:17px;border:1px solid var(--line);display:flex}
.search span{flex:1;font-size:6px;color:#999;padding:4px 7px}
.search b{background:var(--green);color:#fff;font-size:6px;font-weight:600;padding:4px 7px;margin:1px}
.cart{left:602px;top:42px;width:98px;height:17px;border:1px solid var(--line);font-size:6px;color:#777;display:flex;align-items:center;gap:4px;padding-left:8px}
.cart em{color:var(--orange);font-style:normal}

.main-nav{left:15px;top:84px;width:685px;height:32px;background:var(--orange);display:flex;align-items:center}
.nav-products{width:152px;height:32px;background:var(--green);color:#fff;font-weight:600;font-size:10px;display:flex;align-items:center;padding-left:38px;gap:28px;clip-path:polygon(6px 0,140px 0,152px 16px,140px 32px,6px 32px,0 16px)}
.nav-item{height:32px;display:flex;align-items:center;padding:0 22px 0 19px;color:#fff;font-size:8.3px;border-right:1px solid rgba(255,255,255,.25);text-transform:uppercase;position:relative}
.nav-item:last-child{border:0}
.nav-item.current::after{content:"";position:absolute;left:50%;bottom:0;border:4px solid transparent;border-bottom-color:#fff;margin-left:-4px}

.category-list{left:21px;top:126px;width:139px;height:284px;background:var(--orange);list-style:none}
.category-list li{height:28px;line-height:28px;padding-left:11px;font-size:6.6px;color:#fff;text-transform:uppercase;border-bottom:1px solid rgba(255,255,255,.2);white-space:nowrap;overflow:hidden}
.category-list li.active{background:var(--green)}

.hero{left:173px;top:126px;width:527px;height:284px;background:linear-gradient(135deg,#4e7f25 0%,#6d9a39 35%,#8c8c86 55%,#5f8e2f 70%,#7a5a44 100%)}
.hero-copy{position:absolute;left:24px;top:96px;color:#fff}
.hero-title{font-family:"Audiowide",sans-serif;font-size:19px;letter-spacing:.5px}
.hero-sub{font-size:9px;font-weight:700;margin-top:4px}
.hero-text{font-size:7px;line-height:11px;width:200px;margin-top:4px}
.hero-btn{display:inline-block;margin-top:9px;background:var(--green);font-size:8px;font-weight:700;padding:9px 15px}
.hero-arrows{position:absolute;right:21px;top:227px;display:flex;gap:2px}
.hero-arrows span{width:17px;height:17px;background:var(--orange);color:#fff;font-size:9px;text-align:center;line-height:17px}

.contact-title{left:26px;top:437px;font-family:"Audiowide",sans-serif;font-size:13.5px;color:var(--orange)}
.contact-intro{left:26px;top:463px;font-size:7.8px;line-height:18px}
.field{border:1px solid var(--line);display:flex;align-items:center;gap:8px;padding-left:10px;font-size:6.6px;color:#555;text-transform:uppercase}
.field svg{width:9px;height:9px;fill:#777}
.field.tall{align-items:flex-start;padding-top:11px}
.captcha{left:26px;top:675px;width:143px;height:59px;border:1px solid #ccc;background:#f4f4f4}
.refresh{left:184px;top:720px}
.captcha-label{left:208px;top:686px;font-size:6.4px;text-transform:uppercase}
.captcha-input{left:207px;top:700px;width:150px;height:34px;border:1px solid var(--line)}
.submit{left:380px;top:702px;width:103px;height:31px;background:linear-gradient(var(--green),var(--green-dark));color:#fff;font-size:8px;font-weight:700;text-align:center;line-height:31px}
.map{left:26px;top:776px;width:667px;height:205px;border:2px solid #eee;background:linear-gradient(160deg,#e2e2e2,#d2d2d2 55%,#e6e6e6)}

.footer{left:0;top:1012px;width:722px;height:154px;background:var(--footer);color:var(--footer-text)}
.footer-col{position:absolute;top:17px}
.footer-col h4{font-size:8.3px;font-weight:600;color:var(--green);text-transform:uppercase;padding-bottom:6px;border-bottom:1px solid #4a4a4a;margin-bottom:8px}
.links li{font-size:7.2px;line-height:15.2px;list-style:none;padding-left:12px;position:relative}
.links li::before{content:"";position:absolute;left:0;top:6px;width:3px;height:3px;border-radius:50%;background:#fff}
.links li.current{color:var(--green)}
.info-row{display:flex;gap:7px;font-size:7.2px;line-height:13.5px;margin-bottom:6px}
.info-row svg{width:8px;height:8px;fill:var(--orange);flex:none;margin-top:3px}
.info-row strong{color:#fff;font-weight:600;font-size:8px}
.quote-mark{display:block;margin:0 auto;width:10px;height:8px}
.testimonial{font-size:7.2px;line-height:13px;width:156px;margin-top:6px}
.author{font-size:7.6px;line-height:13px;margin-top:6px}
.author b{color:#fff;font-weight:600}
.social{display:grid;grid-template-columns:78px 82px;row-gap:12px;font-size:7.8px}
.social div{display:flex;align-items:center;gap:8px;white-space:nowrap}
.social i{width:19px;height:19px;border-radius:50%;background:var(--orange);flex:none}
.social i.green{background:var(--green)}
.cards{display:flex;gap:4px;margin-top:10px}
.cards span{width:27px;height:15px;border-radius:2px;background:#fff}
.copyright{left:0;top:1166px;width:722px;height:34px;background:var(--orange);color:#fff;font-size:7.3px;text-align:center;line-height:34px}
</style>
</head>
<body>
<div class="page">

  <div class="abs utility-bar">
    <span>Home</span><span class="sep">|</span><span>My Account</span><span class="sep">|</span><span>Login</span><span class="sep">|</span><span>Register</span>
  </div>

  <div class="abs brand">
    <span class="brand-mark"></span>
    <div class="brand-name">Plumbrook Ground Solutions</div>
  </div>

  <div class="abs search"><span>SEARCH YOUR ITEMS :</span><b>SEARCH</b></div>
  <div class="abs cart">
    <svg width="8" height="8" viewBox="0 0 10 10"><path d="M0 1h2l1.5 5h5L10 2H3" fill="none" stroke="#f78f20" stroke-width="1.3"/><circle cx="4" cy="8.5" r="1" fill="#f78f20"/><circle cx="8" cy="8.5" r="1" fill="#f78f20"/></svg>
    YOUR CART IS : <em>0 ITEMS</em>
  </div>

  <nav class="abs main-nav">
    <div class="nav-products">PRODUCTS <span style="font-size:8px">&#8964;</span></div>
    <div class="nav-item" style="padding-left:20px">Shop</div>
    <div class="nav-item">About Us</div>
    <div class="nav-item">Ground Solutions</div>
    <div class="nav-item">Plumbrook</div>
    <div class="nav-item current">Contact Us</div>
  </nav>

  <ul class="abs category-list">
    <li>Geotextile Membranes</li>
    <li class="active">Light Domestic Driveways</li>
    <li>Heavy Domestic Driveways</li>
    <li>Parking and Pathway System</li>
    <li>Grass Reinforcement Mesh &amp;</li>
    <li>Turf Reinforcement Mesh</li>
    <li>Steel U Pins</li>
    <li>Commercial Parking System</li>
    <li>Terralock Grid</li>
    <li>Monthly Specials</li>
  </ul>

  <section class="abs hero" role="img" aria-label="Aerial photo of a curving gravel garden path bordered by lawn, shrubs and timber decking">
    <div class="hero-copy">
      <div class="hero-title">PLUMBROOK ECO</div>
      <div class="hero-sub">SOLUTIONS LTD STABILISED GRAVEL</div>
      <div class="hero-text">Part of a natural porous paving system, when filled with gravel this gives you an eco-friendly</div>
      <div class="hero-btn">VIEW PRODUCT</div>
    </div>
    <div class="hero-arrows"><span>&lsaquo;</span><span>&rsaquo;</span></div>
  </section>

  <h2 class="abs contact-title">CONTACT US AND TRADE ENQUIRY</h2>
  <p class="abs contact-intro">If you require more information please fill in the form below. You will be contacted as soon as possible.<br>Please fill in all required fields.</p>

  <div class="abs field" style="left:26px;top:510px;width:225px;height:32px">
    <svg viewBox="0 0 10 10"><circle cx="5" cy="3" r="2.5"/><path d="M0 10c0-3 2-4.5 5-4.5s5 1.5 5 4.5z"/></svg>Your Name</div>
  <div class="abs field" style="left:272px;top:510px;width:225px;height:32px">
    <svg viewBox="0 0 10 10"><path d="M0 2h10v6H0z M0 2l5 3.5L10 2" stroke="#fff" stroke-width=".6"/></svg>Email Address</div>
  <div class="abs field" style="left:26px;top:553px;width:225px;height:32px">
    <svg viewBox="0 0 10 10"><path d="M2 0l2 2.5-1 1.2c.6 1.3 1.7 2.4 3 3l1.2-1L10 7.8 8.3 10C4 9.6.4 6 0 1.7z"/></svg>Phone</div>
  <div class="abs field" style="left:272px;top:553px;width:225px;height:32px">
    <svg viewBox="0 0 10 10"><circle cx="5" cy="3" r="2.5"/><path d="M0 10c0-3 2-4.5 5-4.5s5 1.5 5 4.5z"/></svg>How did you hear about us?</div>
  <div class="abs field tall" style="left:26px;top:598px;width:471px;height:65px">
    <svg viewBox="0 0 10 10"><path d="M7.5 0L10 2.5 3 9.5H.5V7z"/></svg>Describe your request</div>

  <div class="abs captcha" role="img" aria-label="Distorted captcha lettering"></div>
  <svg class="abs refresh" width="15" height="15" viewBox="0 0 16 16" fill="none" stroke="var(--refresh)" stroke-width="2.2">
    <path d="M13 6A5.5 5.5 0 0 0 3 5"/><path d="M3 10a5.5 5.5 0 0 0 10 1"/><path d="M13 1.5V6H8.5" stroke-width="2"/><path d="M3 14.5V10h4.5" stroke-width="2"/>
  </svg>
  <div class="abs captcha-label">Enter your captcha</div>
  <div class="abs captcha-input"></div>
  <div class="abs submit">SUBMIT</div>

  <div class="abs map" role="img" aria-label="Street map showing the office location and nearby roads"></div>

  <footer class="abs footer">
    <div class="footer-col" style="left:40px;width:95px">
      <h4>Quick Links</h4>
      <ul class="links">
        <li>Shop</li><li class="current">About us</li><li>Ground Solutions</li><li>Plumbrook</li><li>Customer Services</li><li>Request a Quote</li><li>Contact Us</li>
      </ul>
    </div>
    <div class="footer-col" style="left:157px;width:160px">
      <h4>Contact Info</h4>
      <div class="info-row"><svg viewBox="0 0 10 10"><path d="M2 0l2 2.5-1 1.2c.6 1.3 1.7 2.4 3 3l1.2-1L10 7.8 8.3 10C4 9.6.4 6 0 1.7z"/></svg>
        <div><strong>0161-555-0142 | 0800-555-0199</strong><br>24 Hour Messaging Service</div></div>
      <div class="info-row"><svg viewBox="0 0 10 10"><path d="M5 0a3.5 3.5 0 0 1 3.5 3.5C8.5 6 5 10 5 10S1.5 6 1.5 3.5A3.5 3.5 0 0 1 5 0z"/></svg>
        <div>Larchfield House, Marsh Lane Trade Park,<br>Holtbury HB4 2QE</div></div>
      <div class="info-row"><svg viewBox="0 0 10 10"><path d="M0 4.5L10 0 7 10 5 6z"/></svg>
        <div>sales@plumbrookpaving.co.uk<br>Mon to Fri-9.00am to 6.00pm</div></div>
    </div>
    <div class="footer-col" style="left:347px;width:157px">
      <h4>Testimonials</h4>
      <svg class="quote-mark" viewBox="0 0 10 8" fill="#999"><rect x="0" y="0" width="4" height="4"/><path d="M0 4h2v1.5L0 8z"/><rect x="6" y="0" width="4" height="4"/><path d="M6 4h2v1.5L6 8z"/></svg>
      <p class="testimonial">Quality products at an affordable price and which meets the requirements of our customers. We supply a permeable paving system that keeps the traditional</p>
      <p class="author"><b>Dana Whitlow</b>,Manager<br>Keystone Builds</p>
    </div>
    <div class="footer-col" style="left:540px;width:160px">
      <h4>Follow Us</h4>
      <div class="social">
        <div><i></i>Friendhub</div><div><i class="green"></i>Chatterbird</div>
        <div><i></i>Pinboardly</div><div><i></i>Circlesphere</div>
      </div>
      <div class="cards"><span></span><span></span><span></span><span></span><span></span></div>
    </div>
  </footer>

  <div class="abs copyright">©2016. PLUMBROOKPAVING. ALL RIGHTS RESERVED.</div>
</div>
</body>
</html>
```